2009 Thank You

A colorful post card that is 8.5 x 5.5.  The purpose is to say thank you to our customers and to wish them a prosperous new year.  We a printing company and will print 4-color process on both sides of the post card

Requirements
Must have
• I have included our logo to be incorporated where appropriate 

Nice to have
• The theme might incorporate something that recognizes "these are turbulent times"  or "success from adversity"

```html
<!DOCTYPE html>
<html lang="en">
<head>
<meta charset="utf-8">
<title>2009 Thank You Postcard</title>
<link href="https://fonts.googleapis.com/css2?family=Roboto+Condensed:ital,wght@0,400;0,700;1,400;1,700&family=Open+Sans:ital,wght@0,400;1,600&display=swap" rel="stylesheet">
<style>
  :root {
    --sky: #a6ecfc;
    --ink: #000000;
    --paper: #ffffff;
    --airplane-blue: #1a1aff;
    --parachute-red: #ff1a1a;
    --photo-warm: #e8a04a;
    --photo-deep: #c0392b;
  }
  html, body {
    margin: 0;
    padding: 0;
    width: 927px;
    height: 1200px;
    overflow: hidden;
    background: var(--paper);
  }
  .postcard {
    position: relative;
    width: 927px;
    height: 1200px;
    box-sizing: border-box;
    border: 2px solid var(--ink);
    font-family: "Roboto Condensed", sans-serif;
    color: var(--ink);
  }
  .front {
    position: absolute;
    left: 0; top: 0;
    width: 100%;
    height: 598px;
    background: var(--sky);
    border-bottom: 2px solid var(--ink);
  }
  .quote-line {
    position: absolute;
    left: 39px;
    margin: 0;
    white-space: nowrap;
    font-style: italic;
    line-height: 1;
  }
  .quote-line--one { top: 58px; font-size: 21px; }
  .quote-line--two { top: 114px; font-size: 21px; }
  .quote-line--three { top: 186px; left: 572px; font-size: 26px; }
  .open-mark { font-weight: 700; font-size: 26px; vertical-align: 12px; margin-right: 6px; }
  .heavy { font-weight: 700; }
  .big { font-weight: 700; font-size: 34px; }
  .airplane { font-weight: 700; font-size: 34px; color: var(--airplane-blue); }
  .parachute { font-weight: 700; font-size: 38px; color: var(--parachute-red); margin-left: 8px; }
  .close-mark { font-weight: 700; font-size: 30px; vertical-align: 6px; }
  .attribution {
    position: absolute;
    right: 47px;
    top: 227px;
    margin: 0;
    font-size: 14px;
    font-style: italic;
  }
  .photo {
    position: absolute;
    left: 258px;
    top: 228px;
    width: 390px;
    height: 234px;
    border-radius: 45% 45% 40% 40%;
    background: radial-gradient(ellipse at 50% 50%, var(--photo-warm) 0%, var(--photo-deep) 55%, rgba(192,57,43,0) 75%);
  }
  .back { position: absolute; left: 0; top: 600px; width: 100%; height: 598px; }
  .wish {
    position: absolute;
    left: 41px;
    top: 56px;
    margin: 0;
    font-size: 25px;
    font-weight: 700;
    font-style: italic;
    line-height: 58px;
  }
  .stamp-box {
    position: absolute;
    left: 787px; top: 31px;
    width: 95px; height: 108px;
    box-sizing: border-box;
    border: 1.5px solid var(--ink);
  }
  .address-line {
    position: absolute;
    left: 548px;
    width: 227px;
    height: 0;
    border-top: 1.5px solid var(--ink);
  }
  .brand {
    position: absolute;
    left: 53px;
    top: 448px;
    display: flex;
    align-items: center;
    gap: 8px;
  }
  .brand-name { font-size: 40px; font-weight: 700; line-height: 1; }
  .brand-square { width: 16px; height: 16px; background: var(--ink); }
  .brand-tagline {
    position: absolute;
    left: 53px;
    top: 518px;
    margin: 0;
    font-family: "Open Sans", sans-serif;
    font-size: 10px;
    font-weight: 600;
    font-style: italic;
  }
  .thanks {
    position: absolute;
    right: 56px;
    top: 519px;
    margin: 0;
    font-family: "Open Sans", sans-serif;
    font-size: 16px;
  }
</style>
</head>
<body>
<div class="postcard">
  <section class="front">
    <p class="quote-line quote-line--one"><span class="open-mark">&ldquo;</span><span class="heavy">Both</span> <span class="big">optimists</span> and <span class="big">pessimists</span> contribute to our society.</p>
    <p class="quote-line quote-line--two">The <span class="heavy">optimist invents</span> the<span class="airplane">AIRPLANE</span> and the <span class="heavy">pessimist:</span></p>
    <p class="quote-line quote-line--three">the<span class="parachute">PARACHUTE</span>.<span class="close-mark">&rdquo;</span></p>
    <p class="attribution">- M.R. Hale, British novelist</p>
    <div class="photo" role="img" aria-label="Photo of two tandem skydivers in free fall against the sky"></div>
  </section>
  <section class="back">
    <p class="wish">Wishing you a productive and prosperous 2009,<br>no matter how full or empty your glass!</p>
    <div class="stamp-box"></div>
    <div class="address-line" style="top:300px"></div>
    <div class="address-line" style="top:343px"></div>
    <div class="address-line" style="top:386px"></div>
    <div class="brand">
      <span class="brand-name">Inkwell Press</span>
      <span class="brand-square"></span>
    </div>
    <p class="brand-tagline">printing, marketing, direct mail and fulfillment</p>
    <p class="thanks">We Appreciate Your Business.</p>
  </section>
</div>
</body>
</html>
```